Business card por a urban DJ, up scale audience target

Need a sober design, modern, conservative colors but i can consider some options, y play rnb, hip hop, EDM and top40.

Business card for contact and personal info, double sided, use logo attrached please; im 42 so i need a card acording to my age an target audience.

Target Market(s)

Adult people, up scale audience

Industry/Entity Type

Music Download

Contact Information for Business Card

Cel (318) 5024471963 www.kelvarodun.com

Requirements
Must have
• open mind
Nice to have
• open mind
Should not have
• DJ

```html
<!DOCTYPE html>
<html lang="en">
<head>
<meta charset="utf-8">
<title>Kelvaro – Business Card</title>
<link href="https://fonts.googleapis.com/css2?family=Open+Sans:wght@400;600;800&display=swap" rel="stylesheet">
<style>
  :root {
    --page: #e9ecec;
    --ink: #111111;
    --card-black-top: #1c1c1c;
    --card-black-bottom: #050505;
    --card-white: #f4f4f4;
    --band: #1a1a1a;
    --rule: #8a8a8a;
    --text-dark: #1b1b1b;
    --text-light: #ffffff;
  }
  * { margin: 0; padding: 0; box-sizing: border-box; }
  html, body { width: 1200px; height: 900px; overflow: hidden; }
  body {
    background: var(--page);
    font-family: "Open Sans", Arial, sans-serif;
    display: flex;
    flex-direction: column;
    align-items: center;
    justify-content: center;
    gap: 40px;
  }
  .card {
    position: relative;
    width: 700px;
    height: 400px;
    box-shadow: 0 6px 18px rgba(0,0,0,0.12);
    overflow: hidden;
  }
  .card-front {
    background: radial-gradient(ellipse at 50% 45%, var(--card-black-top), var(--card-black-bottom) 75%);
    display: flex;
    align-items: center;
    justify-content: center;
  }
  .brand-name {
    font-weight: 800;
    letter-spacing: 4px;
    text-transform: uppercase;
  }
  .card-front .brand-name {
    color: var(--text-light);
    font-size: 64px;
  }
  .card-back { background: var(--card-white); }
  .side-band {
    position: absolute;
    left: 0; top: 0; bottom: 0;
    width: 38px;
    background: linear-gradient(90deg, #262626, var(--band));
  }
  .card-back .brand-name {
    position: absolute;
    right: 48px;
    top: 48px;
    color: var(--text-dark);
    font-size: 40px;
  }
  .rule {
    position: absolute;
    height: 1px;
    background: var(--rule);
  }
  .rule-top { right: 40px; width: 250px; top: 130px; }
  .rule-mid { right: 40px; width: 330px; top: 240px; }
  .contact-list {
    position: absolute;
    left: 66px;
    bottom: 44px;
    list-style: none;
    display: flex;
    flex-direction: column;
    gap: 10px;
  }
  .contact-item {
    display: flex;
    align-items: center;
    gap: 12px;
    font-size: 17px;
    font-weight: 600;
    color: var(--text-dark);
  }
  .contact-icon { width: 18px; height: 18px; flex: none; }
</style>
</head>
<body>
  <section class="card card-front">
    <span class="brand-name">Kelvaro</span>
  </section>

  <section class="card card-back">
    <div class="side-band"></div>
    <span class="brand-name">Kelvaro</span>
    <div class="rule rule-top"></div>
    <div class="rule rule-mid"></div>
    <ul class="contact-list">
      <li class="contact-item">
        <svg class="contact-icon" viewBox="0 0 18 18" aria-hidden="true">
          <rect x="4.5" y="1.5" width="9" height="15" rx="1.5" fill="none" stroke="#555" stroke-width="1.4"/>
          <line x1="7.5" y1="14" x2="10.5" y2="14" stroke="#555" stroke-width="1.2"/>
        </svg>
        <span>(318) 5024471963</span>
      </li>
      <li class="contact-item">
        <svg class="contact-icon" viewBox="0 0 18 18" aria-hidden="true">
          <circle cx="9" cy="9" r="8" fill="#555"/>
          <g fill="none" stroke="#f4f4f4" stroke-width="0.9">
            <ellipse cx="9" cy="9" rx="3.5" ry="8"/>
            <line x1="1" y1="9" x2="17" y2="9"/>
            <line x1="2.5" y1="5" x2="15.5" y2="5"/>
            <line x1="2.5" y1="13" x2="15.5" y2="13"/>
          </g>
        </svg>
        <span>www.kelvarodun.com</span>
      </li>
    </ul>
  </section>
</body>
</html>
```